Tri Fold Brochure - Sunny Grove - wellbeing coaching

Hello design gurus!
I'm after a tri fold brochure for my business that provides wellbeing coaching for helping people change behaviours and habits such as quitting smoking and weight loss. I also provide general life coaching.
Please provide tri fold brochure design as per the following:
- A4, double sided
- Design that works both in colour and black & white
- Business name (Sunny Grove) logo attached
- Logo tag line is: Enhance your life with Wellbeing Coaching
- Brochure to complement logo and logo colours
- Professional look and feel
- Health, wellbeing, living a great life look and feel
- Written content attached but please change layout to whatever is better. Image in content does not have to be used.
- Open to all suggestions regarding content, layout, images, colours etc
Looking forward to receiving your design!
Kind Regards,
Marcus

```html
<!DOCTYPE html>
<html lang="en">
<head>
<meta charset="utf-8">
<title>Sunny Grove – Wellbeing Coaching Brochure</title>
<link href="https://fonts.googleapis.com/css2?family=PT+Sans:wght@400;700&family=Tinos&display=swap" rel="stylesheet">
<style>
  :root{
    --cyan:#29c3ea;
    --green:#8cc43f;
    --green-light:#b5d96b;
    --heading-blue:#1eaee0;
    --heading-green:#8cbf3a;
    --body:#5d5d5d;
    --footer-text:#5b6b3a;
    --paper:#ffffff;
  }
  *{box-sizing:border-box;margin:0;padding:0}
  html,body{width:1200px;height:933px;overflow:hidden;background:var(--paper)}
  .brochure{position:relative;width:1200px;height:933px;overflow:hidden;background:var(--paper);
    font-family:"PT Sans",Arial,sans-serif;font-weight:700;color:var(--body)}
  .bands{position:absolute;inset:0}
  .swirl{position:absolute;left:330px;top:200px;width:780px;height:520px;border-radius:50%;
    background:radial-gradient(ellipse at center,rgba(200,200,200,.35) 0%,rgba(220,220,220,.18) 45%,rgba(255,255,255,0) 70%)}
  .panel-title{position:absolute;left:24px;top:34px;font-family:"Tinos",serif;font-size:24px;
    color:#fff;transform:rotate(-10deg);transform-origin:left top}
  .col{position:absolute;text-align:center;font-size:15px;line-height:22px}
  .col p{margin-bottom:10px}
  .col-left{left:34px;top:104px;width:334px}
  .col-centre{left:436px;top:58px;width:342px}
  .col-right{left:812px;top:72px;width:362px}
  .quote{font-weight:400;color:#555;font-size:16px;line-height:22px}
  .gap{margin-bottom:18px!important}
  .tight{margin-bottom:2px!important}
  .h-blue{color:var(--heading-blue);font-size:18px;line-height:22px;margin:4px 0 6px}
  .h-green{font-family:"Tinos",serif;font-weight:400;color:var(--heading-green);font-size:23px;line-height:28px;margin:2px 0 4px}
  .h-green.lead{font-size:24px;line-height:29px}
  .footer-line{position:absolute;left:0;width:1200px;top:872px;text-align:center;
    font-size:19px;color:var(--footer-text);transform:rotate(1.5deg)}
</style>
</head>
<body>
<main class="brochure">
  <div class="swirl" role="img" aria-label="Soft grey floral swirl decoration behind the panels"></div>

  <svg class="bands" width="1200" height="933" viewBox="0 0 1200 933" aria-hidden="true">
    <path d="M0 0 H600 C420 25 220 55 0 120 Z" fill="var(--green)"/>
    <path d="M0 0 H560 C400 18 200 40 0 100 Z" fill="var(--cyan)"/>
    <path d="M740 0 H1200 V70 C1080 25 900 8 740 0 Z" fill="var(--green)"/>
    <path d="M770 0 H1200 V55 C1080 18 920 4 770 0 Z" fill="var(--cyan)"/>
    <path d="M0 848 C320 800 760 888 1200 808 V933 H0 Z" fill="var(--green-light)"/>
    <path d="M0 860 C320 816 760 902 1200 830 V933 H0 Z" fill="var(--green)"/>
    <path d="M0 908 C340 884 760 944 1200 884 V933 H0 Z" fill="var(--cyan)"/>
  </svg>

  <div class="panel-title">Client Comments</div>

  <section class="col col-left">
    <p class="quote tight">“Their ways of helping you works. It’s simple yet very effective and I feel great” - Jonah</p>
    <p class="quote gap">“It was very well constructed and delivered and also enjoyable. It worked too!” - Callum</p>
    <p class="quote gap">“It was simple, logical and a positive experience. It has been successful” - Dale</p>
    <p class="quote gap">“It helps me to have a longer, happier life. Very easy to accept that my days of being unfit are over” - Fergus</p>
    <p class="quote tight">“I feel positive about the future. Marcus was easy to relate to and I felt relaxed and confident from the beginning of the session” - Leanne</p>
    <h2 class="h-blue">Would you like to improve your life in some way?</h2>
    <p class="tight">Whether you’d like to lose weight or improve your health through more healthy eating and enjoyable exercise, or quitting smoking, decrease stress, change any habits or you simply desire more peace, fulfilment or achievement in your life, then Sunny Grove coaching can enable you to do all this and more.</p>
    <h2 class="h-green">Stress Reduction</h2>
    <p>Too much stress can damage health, the immune system, contribute to disease and illness, damage relationships and result in ineffective actions. Our stress reduction program enables our clients to get very clear on the cause of their stress and how to reduce it through effective mind, behavioural and life change approaches.</p>
  </section>

  <section class="col col-centre">
    <h1 class="h-green lead">Breathe Free in 60 Minutes. Guaranteed.</h1>
    <p style="margin-bottom:20px">The main methods of quitting smoking – will power, nicotine patches, drugs – don’t work for most people. This is because the main cause of smoking is the mental habit. As habits are largely run by the unconscious mind, it is hard to quit smoking when the method used doesn’t remove the unconscious automatic habit.</p>
    <p style="margin-bottom:20px">The Breathe Free in 60 Minutes system uses the powerful combination of NLP and hypnotherapy to remove the desire and habit of smoking. Our clients become Non-smokers and not ex-smokers who still want to smoke.</p>
    <p style="margin-bottom:30px">Because the success rate is very high we can offer a guarantee that means if any follow up sessions are required then these are free of charge.</p>
    <h2 class="h-green" style="margin-bottom:20px">How are life changes made?</h2>
    <p>Your behaviours and actions significantly influence the life you live. What determines your behaviours are your patterns of thinking and feeling that have a hold on you. Addressing these thinking and feeling patterns can bring about the behaviour and life changes that are important to you. This can be difficult to do on your own as many of your thinking and feeling patterns are automatic.</p>
  </section>

  <section class="col col-right">
    <h2 class="h-blue" style="margin-top:0">Mindfulness, Fulfilment and Achievement Coaching</h2>
    <p>This approach to life coaching enables living with qualities such as greater fulfilment, vitality, balance, meaningfulness, purpose and success. It is easy for the busy-ness of life to take us away from what’s most important. This coaching helps you live the life you truly want across the various areas of your life - for example health, relationships, finances, work, rest and fun.</p>
    <h2 class="h-green">Weight Loss</h2>
    <p class="tight">Weight gain, unhealthy eating and lack of exercise are often caused by unhelpful thinking and emotional patterns. Our Fresh Start program addresses these patterns which enables our clients to be in charge of their own healthy nutrition and desired physical activities.</p>
    <h2 class="h-blue" style="margin-top:0">What methods are used?</h2>
    <p style="margin-bottom:22px">The approaches used include Neuro Linguistic Programming (NLP), mindfulness, hypnotherapy &amp; life coaching. These are all very easy, safe and effective approaches to changing behaviours and giving you much greater empowerment in living the life you want.</p>
    <h2 class="h-green">The Unconscious Mind</h2>
    <p>Your automatic habits are largely run by your unconscious mind. This is why many people struggle to make changes with only their conscious mind as their unconscious mind is still running the old, unhelpful, automatic habits. Ease and speed of change is greatly enhanced by also addressing these unconscious habits</p>
  </section>

  <div class="footer-line">Acclerated Certification Course in Clinical Hypnotherapy</div>
</main>
</body>
</html>
```